Health Coach needs a creative and catchy Chatnook Ad Image to increase page likes

I have just recently launched a health coaching business and would like to increase my Chatnook awareness and page likes.
I plan on doing a “page liking” campaign through Chatnook and want a creative, catchy and unique image to help make my campaign successful.
I want a versatile image, as I am aiming to run this campaign on Chatnook for a while (few months).
The image is to be 1200 x 444 pixels, with an image ratio of 8:3, and because it is going on Chatnook it cannot have any overlaid text (or very little).
So, the image will have to be very visually appealing and catchy!
I am happy for some creative illustrations and drawings to be used to help portray my message (please see attached for some sample pictures)
I would like the image to portray the following:
-health
-happiness
-change
Some of my key messages that you could include:
-holistic health
-health & wellness
-health, nutrition, lifestyle
-Food, fitness, happiness

In addition, a call to action that could be incorporated could be:
"i can help you"
..or something similar (but only if this can fit).

I have attached some images of myself to be used.

Target Market(s)

People looking for health and fitness advice

Industry/Entity Type

Health And Wellness

Colors

Requirements
Nice to have
• illustrations as per 2 sample images provided
• call to action if can fit

```html
<!DOCTYPE html>
<html lang="en">
<head>
<meta charset="utf-8">
<title>Health Coach – I can help you</title>
<link rel="stylesheet" href="https://fonts.googleapis.com/css2?family=Gochi+Hand&family=Great+Vibes&display=swap">
<style>
  :root {
    --canopy-dark: #1f2a17;
    --canopy: #33451f;
    --lawn-far: #5d8430;
    --lawn: #6e9a3a;
    --lawn-near: #557a2b;
    --path: #8a8f6a;
    --hair: #8a5a35;
    --skin: #d9ad8c;
    --shirt: #eef0ea;
    --jeans: #1f2b4a;
    --word: #ffffff;
    --cta: #22241a;
  }
  html, body {
    margin: 0;
    padding: 0;
    width: 1200px;
    height: 444px;
    overflow: hidden;
    background: var(--canopy-dark);
  }
  .banner {
    position: relative;
    width: 1200px;
    height: 444px;
    overflow: hidden;
  }
  .banner__scene {
    position: absolute;
    inset: 0;
    background:
      radial-gradient(ellipse 900px 380px at 600px 260px, rgba(0, 0, 0, 0), rgba(0, 0, 0, 0.35) 100%),
      linear-gradient(180deg,
        var(--canopy-dark) 0%,
        var(--canopy) 18%,
        var(--lawn-far) 32%,
        var(--lawn) 44%,
        var(--path) 47%,
        var(--lawn) 50%,
        var(--lawn) 75%,
        var(--lawn-near) 100%);
  }
  .coach-photo {
    position: absolute;
    left: 440px;
    top: 10px;
    width: 266px;
    height: 420px;
    border-radius: 120px 120px 40px 40px;
    background: linear-gradient(180deg,
      var(--hair) 0%,
      var(--skin) 22%,
      var(--shirt) 36%,
      var(--shirt) 72%,
      var(--jeans) 80%,
      var(--jeans) 100%);
    opacity: 0.9;
  }
  .keyword {
    position: absolute;
    margin: 0;
    font-family: "Gochi Hand", cursive;
    font-size: 34px;
    line-height: 1;
    color: var(--word);
    white-space: nowrap;
  }
  .keyword--wellness  { left: 283px; top: 32px;  transform: rotate(14deg); }
  .keyword--change    { left: 232px; top: 124px; transform: rotate(8deg); }
  .keyword--nutrition { left: 168px; top: 198px; transform: rotate(8deg); }
  .keyword--lifestyle { left: 126px; top: 290px; transform: rotate(-5deg); }
  .keyword--food      { left: 823px; top: 76px;  transform: rotate(-14deg); }
  .keyword--happiness { left: 884px; top: 136px; transform: rotate(-10deg); }
  .keyword--fitness   { left: 930px; top: 226px; transform: rotate(-5deg); }
  .keyword--holistic  { left: 946px; top: 322px; }
  .call-to-action {
    position: absolute;
    left: 486px;
    top: 228px;
    margin: 0;
    font-family: "Great Vibes", cursive;
    font-size: 58px;
    font-weight: 400;
    line-height: 1;
    color: var(--cta);
    white-space: nowrap;
  }
</style>
</head>
<body>
  <main class="banner">
    <div class="banner__scene" role="img" aria-label="Sunlit park lawn with trees behind and a line-drawn lotus flower fanning out around the centre"></div>
    <div class="coach-photo" role="img" aria-label="Photograph of the health coach sitting cross-legged on the grass in a white top and navy jeans"></div>

    <p class="keyword keyword--wellness">wellness</p>
    <p class="keyword keyword--change">change</p>
    <p class="keyword keyword--nutrition">nutrition</p>
    <p class="keyword keyword--lifestyle">lifestyle</p>

    <p class="keyword keyword--food">Food</p>
    <p class="keyword keyword--happiness">happiness</p>
    <p class="keyword keyword--fitness">fitness</p>
    <p class="keyword keyword--holistic">holistic health</p>

    <h1 class="call-to-action">i can help you</h1>
  </main>
</body>
</html>
```